Moll's RV Park & Lodge Rack Card

Moll’s RV Park & Lodge
Highway 9
Leeds ND
701-555-0183
www.mollsbarnyardrvstop.example
mollsbarnyard@mailbox.example

MOLL’S RV PARK
14 Full Service Spaces
• Electric, Water, Sewer
• Safe & convenient location
• 24 hour indoor restroom with shower
• Roadway Circle accepted

Please note: Moll’s RV Park is an unattended RV park. No reservations required. Please pull on in,
use our self-service check-in and then sit back and relax!

MOLL’S LODGE
• Groups – hunting, fishing, working, playing
• 2 restrooms, one is handicap accessible
• Sleeps 15 – 2 bedrooms plus a shared sleeping area with bunk beds

WHERE ARE WE?
We are located right next to Highway 9 on the north side. Take the second (middle) Leeds exit.
 30 miles west of Devils Lake (the town) on Hwy 9
 10 miles west of Devils Lake (the water) on Hwy 9
 30 miles east of Rugby
 60 miles south of the Borderland Bloom Grounds - Manitoba border on Hwy 417

Target Market(s)

RVers and travelers looking for overnight accommodations

Requirements
Must have
• Must have colorful eye catching top 1/3 of card.
• Must have map (can be cropped) that I have included in files.

```html
<!DOCTYPE html>
<html lang="en">
<head>
<meta charset="utf-8">
<title>Moll's RV Park &amp; Lodge Rack Card</title>
<link rel="stylesheet" href="https://fonts.googleapis.com/css2?family=Alegreya+Sans+SC:wght@700&family=Archivo+Black&family=Archivo+Narrow:wght@700&family=Arimo:ital,wght@0,400;1,700&family=Lilita+One&family=Luckiest+Guy&family=Raleway:wght@300&family=Yellowtail&display=swap">
<style>
:root{
  --red:#c3202b;
  --dark-red:#8c1a1f;
  --orange:#f2a23a;
  --gold:#f6b24b;
  --peach:#f2a07c;
  --white:#ffffff;
  --ink:#1d1d1d;
}
*{margin:0;padding:0;box-sizing:border-box}
html,body{width:1200px;height:2613px;overflow:hidden;background:var(--red)}
.card{position:relative;width:1200px;height:2613px;background:var(--red);overflow:hidden;font-family:'Arimo',Arial,sans-serif}
.shapes{position:absolute;inset:0}
.abs{position:absolute}

.headline{left:0;top:85px;width:1200px;text-align:center;font-family:'Lilita One','Arial Black',sans-serif;font-weight:400;transform:rotate(-3deg);line-height:1;white-space:nowrap}
.headline .line1{font-size:82px;color:var(--gold);letter-spacing:2px}
.headline .line2{font-size:92px;color:var(--white);margin-top:10px;letter-spacing:2px}

.oval{display:flex;flex-direction:column;align-items:center;justify-content:center;text-align:center;border-radius:50%;line-height:1.05;white-space:nowrap}
.oval-club{left:275px;top:425px;width:325px;height:170px;background:var(--red);border:6px solid var(--orange);color:var(--gold);font-style:italic;font-weight:700;font-size:32px;transform:rotate(-4deg)}
.oval-safe{left:690px;top:415px;width:440px;height:155px;background:var(--red);border:6px solid var(--orange);color:var(--white);transform:rotate(-9deg)}
.oval-safe .big{font-family:'Luckiest Guy','Arial Black',sans-serif;font-size:46px}
.oval-safe .small{font-style:italic;font-weight:700;font-size:32px}
.oval-restroom{left:845px;top:865px;width:285px;height:150px;background:var(--orange);color:var(--dark-red);font-family:'Luckiest Guy','Arial Black',sans-serif;font-size:31px;transform:rotate(-18deg)}
.oval-spaces{left:72px;top:893px;width:320px;height:180px;background:var(--orange);border:6px solid var(--red);color:var(--dark-red)}
.oval-spaces .big{font-family:'Luckiest Guy','Arial Black',sans-serif;font-size:48px}
.oval-spaces .small{font-style:italic;font-weight:700;font-size:32px}
.oval-hookups{left:420px;top:950px;width:350px;height:155px;background:var(--red);border:7px solid var(--white);color:var(--white);font-family:'Luckiest Guy','Arial Black',sans-serif;font-size:38px;transform:rotate(-4deg)}

.notice{left:88px;top:1205px;width:1000px;color:var(--white);transform:rotate(-4deg);transform-origin:left top;white-space:nowrap}
.notice .label{font-weight:700;font-style:italic;color:var(--orange);font-size:38px}
.notice .label span{font-weight:400;color:var(--white);font-size:33px}
.notice .headline-small{font-family:'Archivo Narrow','Arial Narrow',sans-serif;font-weight:700;font-size:62px;line-height:1.05;letter-spacing:1px}
.notice .body{font-style:italic;font-size:32px;line-height:1.3}

.map{left:0;top:1420px;width:765px;height:500px;background:linear-gradient(160deg,#f7f8f5,#e9ede4 60%,#dfe8ef)}

.directions{left:75px;top:1915px;width:690px;height:157px;background:var(--dark-red);border-top-left-radius:70px;color:var(--orange);font-style:italic;font-weight:700;font-size:27px;line-height:1.3;text-align:center;padding-top:24px}

.located{left:765px;top:1370px;width:355px;text-align:center;color:var(--dark-red)}
.located .title{font-family:'Yellowtail',cursive;font-weight:400;color:var(--white);font-size:62px;margin-bottom:18px}
.located .item{margin-bottom:26px;line-height:1.2}
.located .caps{font-family:'Alegreya Sans SC',sans-serif;font-weight:700;font-size:27px}
.located .plain{font-size:26px}

.name-band{left:75px;top:2072px;width:1045px;height:170px;background:var(--peach);display:flex;align-items:center;justify-content:center;overflow:hidden}
.name-band .name{font-family:'Yellowtail',cursive;font-size:96px;line-height:1;color:var(--ink);white-space:nowrap}

.contact{left:75px;width:1045px;display:flex;align-items:center;justify-content:center;white-space:nowrap}
.contact-address{top:2255px;height:70px;background:var(--dark-red);color:var(--peach);font-family:'Raleway',sans-serif;font-weight:300;font-size:40px}
.contact-phone{top:2325px;height:85px;background:var(--dark-red);color:var(--orange);font-family:'Archivo Black',sans-serif;font-size:54px;letter-spacing:2px}
.contact-web{top:2410px;height:60px;background:var(--orange);color:var(--dark-red);font-family:'Archivo Black',sans-serif;font-size:34px}
.contact-email{top:2470px;height:70px;background:var(--dark-red);color:var(--peach);font-family:'Raleway',sans-serif;font-weight:300;font-size:35px}
.road{left:0;top:2540px;width:1200px;height:73px;background:linear-gradient(180deg,#b9b6b0,#8f8d88)}
</style>
</head>
<body>
<main class="card">
  <svg class="shapes" width="1200" height="2613" viewBox="0 0 1200 2613" aria-hidden="true">
    <path d="M0 470 C300 360 700 300 1200 320 L1200 360 C700 350 320 420 0 540 Z" fill="var(--orange)"/>
    <path d="M0 540 C320 420 700 350 1200 360 L1200 1010 C900 920 420 880 0 900 Z" fill="#9fc4df"/>
    <rect x="765" y="1300" width="355" height="772" fill="var(--orange)"/>
    <rect x="0" y="1915" width="75" height="625" fill="var(--dark-red)"/>
  </svg>
  <div class="abs photo" role="img" aria-label="Photo of RVs and trailers parked on gravel spaces beside a lawn with trees" style="left:0;top:520px;width:1200px;height:480px;background:linear-gradient(180deg,#bcd3e6 0%,#d9e4ea 25%,#4f6d3a 32%,#dcd9d2 55%,#c9c2b3 68%,#6f9a3c 76%,#5a8a2f 100%);clip-path:path('M0 20 C320 -100 700 -170 1200 -160 L1200 480 C900 400 420 360 0 380 Z')"></div>

  <h1 class="abs headline">
    <div class="line1">LOCATED SMACK DAB IN</div>
    <div class="line2">THE MIDDLE OF IT ALL!!</div>
  </h1>

  <div class="abs oval oval-club">Roadway Circle<br>ACCEPTED</div>
  <div class="abs oval oval-safe"><span class="big">SAFE &amp;</span><span class="small">convenient location</span></div>
  <div class="abs oval oval-restroom">24H indoor<br>restroom<br>with shower</div>
  <div class="abs oval oval-spaces"><span class="big">14 FULL</span><span class="small">Service Spaces</span></div>
  <div class="abs oval oval-hookups">ELECTRIC,<br>WATER, SEWER</div>

  <section class="abs notice">
    <p class="label">Please note: <span>Moll’s RV Park is an unattended RV park.</span></p>
    <p class="headline-small">NO RESERVATIONS REQUIRED.</p>
    <p class="body">Please pull on in, use our self-service check-in and<br>&nbsp;then sit back and relax!</p>
  </section>

  <div class="abs map" role="img" aria-label="Road map of the area around Leeds, ND, showing Highway 9 and nearby towns with a star marking the park"></div>
  <p class="abs directions">We are located right next to Highway 9<br>on the north side.<br>Take the second (middle) Leeds exit.</p>

  <section class="abs located">
    <h2 class="title">Located</h2>
    <p class="item"><span class="caps">30 miles west of<br>Devils Lake</span><br><span class="plain">(the town) on Hwy 9</span></p>
    <p class="item"><span class="caps">10 miles west of<br>Devils Lake</span><br><span class="plain">(the water) on Hwy 9</span></p>
    <p class="item"><span class="caps">30 miles east<br>of Rugby</span></p>
    <p class="item"><span class="caps">60 miles south of<br>the Borderland Bloom<br>Grounds</span><br><span class="plain">Manitoba border on<br>Hwy 417</span></p>
  </section>

  <div class="abs name-band"><span class="name">Moll’s RV Park &amp; Lodge</span></div>
  <div class="abs contact contact-address">Highway 9, Leeds ND</div>
  <div class="abs contact contact-phone">701-555-0183</div>
  <div class="abs contact contact-web">WWW.MOLLSBARNYARDRVSTOP.EXAMPLE</div>
  <div class="abs contact contact-email">mollsbarnyard@mailbox.example</div>
  <div class="abs road" role="img" aria-label="Strip of asphalt road with a yellow centre line"></div>
</main>
</body>
</html>
```